Website for IT consulting Company

I need a website upgrade, the existing site content is ok, I would also like to add a testimonial page, the site should be something that is easy for us to update content. You use the content from www.velmarketa.com as an example. I will also post update logo and artwork. I also need a contact form with some type of validation or captcha.

Please omit Address maps

Target Market(s)

small business, service oriented companies. We provide IT Consulting, support and mangement

Industry/Entity Type

Information Technology

Coding

Coded - Design and coding required

Number of Pages Required

1 page

Font styles to use
Serif
Sans Serif

Requirements
Must have
• Contain logo attached, and content from existing web site www.velmarketa.com.
• Also need to update content easily, and be movable to different platforms.
• There is a catch phrase
• "Let us worry about your technology…” “ so you don’t have to!”
• Should be included.
Nice to have
• Testimonial page, Project page where we can post new and past projects and pictures
Should not have
• none

```html
<!DOCTYPE html>
<html lang="en">
<head>
<meta charset="utf-8">
<title>Velmarketa – IT Consulting</title>
<link href="https://fonts.googleapis.com/css2?family=Roboto:wght@300;400;500&display=swap" rel="stylesheet">
<style>
:root{
  --orange:#f29b30;
  --ink:#2b2f36;
  --text:#6b6f76;
  --line:#e4e6ea;
  --soft:#f3f4f6;
  --footer:#2a303c;
  --footer-text:#c9ccd3;
  --white:#ffffff;
}
*{margin:0;padding:0;box-sizing:border-box}
html,body{width:1200px;height:2344px;overflow:hidden}
body{font-family:'Roboto',Arial,sans-serif;color:var(--ink);background:var(--white);position:relative}
.abs{position:absolute}

/* header */
.site-header{position:absolute;top:0;left:0;width:1200px;height:70px;background:var(--white)}
.brand{position:absolute;left:89px;top:20px;display:flex;align-items:center;gap:10px;font-size:24px;font-weight:500;color:var(--orange);letter-spacing:.5px}
.brand-mark{width:22px;height:22px;background:var(--orange);border-radius:4px}
.main-nav{position:absolute;top:27px;left:0;width:1200px;height:20px;font-size:13px;color:var(--ink)}
.main-nav span{position:absolute;top:0}

/* hero */
.hero{position:absolute;top:70px;left:0;width:1200px;height:435px;background:linear-gradient(100deg,#6d6a66 0%,#a9a49c 35%,#d8d4cc 65%,#c5b89e 100%)}
.hero-kicker{position:absolute;left:88px;top:150px;font-size:18px;font-weight:300;color:var(--white)}
.hero-title{position:absolute;left:88px;top:174px;font-size:44px;font-weight:300;color:var(--white)}
.btn{position:absolute;display:flex;align-items:center;justify-content:center;gap:14px;background:var(--white);color:var(--ink);font-size:13px;border-radius:3px}
.btn svg{width:12px;height:10px}

/* outsourcing */
.section-title{position:absolute;left:0;width:1200px;text-align:center;font-size:28px;font-weight:300;color:var(--ink)}
.title-rule{position:absolute;left:580px;width:40px;height:1px;background:var(--line)}
.intro{position:absolute;left:219px;top:627px;width:762px;text-align:center;font-size:13px;line-height:22px;color:var(--text)}
.feature{position:absolute;top:750px;width:330px}
.feature svg{width:40px;height:40px}
.feature h3{margin-top:28px;font-size:20px;font-weight:400;line-height:23px;color:var(--ink)}
.feature p{margin-top:12px;font-size:12.5px;line-height:22px;color:var(--text)}

/* split band */
.office-photo{position:absolute;top:997px;left:0;width:600px;height:389px;background:linear-gradient(120deg,#8c7a66 0%,#c9b59a 45%,#9c7048 75%,#e6ddd0 100%)}
.flex-panel{position:absolute;top:997px;left:600px;width:600px;height:389px;background:var(--orange);color:var(--white)}
.flex-panel h2{position:absolute;left:72px;top:55px;font-size:25px;font-weight:400;line-height:31px}
.flex-panel .rule{position:absolute;left:72px;top:131px;width:40px;height:1px;background:rgba(255,255,255,.6)}
.flex-panel p{position:absolute;left:72px;top:152px;width:450px;font-size:12.5px;line-height:22px}

/* solutions */
.solutions{position:absolute;top:1386px;left:0;width:1200px;height:548px;background:var(--soft)}
.card{position:absolute;width:189px;height:172px;background:var(--white);text-align:center}
.card svg{position:absolute;left:69px;top:36px;width:52px;height:52px}
.card span{position:absolute;left:0;top:112px;width:189px;font-size:15px;line-height:22px;color:var(--ink)}
.card.active{box-shadow:0 14px 24px rgba(40,50,80,.12)}

/* footer */
.site-footer{position:absolute;top:1934px;left:0;width:1200px;height:410px;background:var(--footer);color:var(--footer-text)}
.site-footer h4{position:absolute;top:57px;font-size:17px;font-weight:400;color:var(--white)}
.info-item{position:absolute;left:89px;display:flex;gap:10px;font-size:12.5px;line-height:22px}
.info-item svg{width:12px;height:12px;margin-top:5px;flex:none}
.divider{position:absolute;left:511px;top:35px;width:1px;height:297px;background:#3a414e}
.field-label{position:absolute;font-size:14px;color:var(--white)}
.field-hint{position:absolute;font-size:11px;color:var(--footer-text)}
.field-line{position:absolute;height:1px;background:#444b58}
.captcha{position:absolute;left:622px;top:263px;width:183px;height:44px;background:#f9f9f9;border:1px solid #d3d3d3;border-radius:2px;color:#333;font-size:9px}
.captcha .box{position:absolute;left:8px;top:13px;width:17px;height:17px;border:2px solid #c1c1c1;background:var(--white)}
.captcha .txt{position:absolute;left:32px;top:16px}
.captcha .badge{position:absolute;right:10px;top:9px;width:22px;height:22px;background:#b9c3d6;border-radius:3px}
.submit{position:absolute;left:997px;top:263px;width:114px;height:44px;background:var(--orange);color:var(--white);font-size:13px;display:flex;align-items:center;justify-content:center;gap:14px;border-radius:3px}
.footer-rule{position:absolute;left:89px;top:360px;width:1022px;height:1px;background:#3a414e}
.copyright{position:absolute;top:377px;width:1200px;text-align:center;font-size:12px;color:var(--white)}
</style>
</head>
<body>

<header class="site-header">
  <div class="brand"><span class="brand-mark"></span>Velmarketa</div>
  <nav class="main-nav">
    <span style="left:531px">About us</span>
    <span style="left:616px">Projects</span>
    <span style="left:695px">Support</span>
    <span style="left:772px">Clients</span>
    <span style="left:844px">Careers</span>
    <span style="left:920px">Testimonials</span>
    <span style="left:1025px">Contact</span>
    <span style="left:1098px;top:-1px">
      <svg width="15" height="15" viewBox="0 0 15 15" fill="none" stroke="#2b2f36" stroke-width="1.5"><circle cx="6" cy="6" r="4.5"/><path d="M9.5 9.5L14 14"/></svg>
    </span>
  </nav>
</header>

<section class="hero" role="img" aria-label="Photo of a team meeting: people with laptops listening to a presenter in a bright office">
  <p class="hero-kicker">Let us worry about your technology...</p>
  <h1 class="hero-title">So you don't have to</h1>
  <a class="btn" style="left:89px;top:247px;width:133px;height:44px">Contact us
    <svg viewBox="0 0 12 10" fill="none" stroke="#2b2f36" stroke-width="1.2"><path d="M0 5h11M7 1l4 4-4 4"/></svg>
  </a>
</section>

<h2 class="section-title" style="top:561px">What is outsourcing</h2>
<div class="title-rule" style="top:608px"></div>
<p class="intro">Outsourcing is subcontracting a process, such as product design or manufacturing, to a third-party company.[1] The decision to outsource is often made in the interest of lowering firm costs, redirecting or conserving energy directed at the competencies of a particular business, or to make more efficient use of land, labor, capital, (information) technology and resources. Outsourcing became part of the business lexicon during the 1980s.</p>

<div class="feature" style="left:88px">
  <svg viewBox="0 0 40 40" fill="none" stroke="#2b2f36" stroke-width="1.4">
    <path d="M2 6h36M2 20h36M2 34h36"/>
    <circle cx="12" cy="6" r="3.5" fill="#fff" stroke="#f29b30"/>
    <circle cx="26" cy="20" r="3.5" fill="#fff" stroke="#f29b30"/>
    <circle cx="16" cy="34" r="3.5" fill="#fff" stroke="#f29b30"/>
  </svg>
  <h3>Managed IT Solutions</h3>
  <p>Our staff will design, service, administer and maintain your IT needs. We are well versed on all major operating system, and network appliances.</p>
</div>
<div class="feature" style="left:452px">
  <svg viewBox="0 0 40 40" fill="none" stroke="#2b2f36" stroke-width="1.4">
    <rect x="2" y="2" width="16" height="12"/><path d="M10 14v4M6 18h8"/>
    <rect x="20" y="20" width="16" height="12"/><path d="M28 32v4M24 36h8"/>
    <path d="M24 6h6v8" stroke="#f29b30"/><path d="M16 26h-4v-6" stroke="#f29b30"/>
  </svg>
  <h3>Remote Diagnostic and Support</h3>
  <p>With our live remote-assistance tool, a member of our support team can view your desktop and share control of your mouse and keyboard to get you on your way to a solution.</p>
</div>
<div class="feature" style="left:855px">
  <svg viewBox="0 0 40 40" fill="none" stroke="#2b2f36" stroke-width="1.4">
    <rect x="15" y="2" width="10" height="8" stroke="#f29b30"/>
    <path d="M20 10v8M6 18h28M6 18v8M20 18v8M34 18v8"/>
    <rect x="1" y="26" width="10" height="8"/><rect x="15" y="26" width="10" height="8"/><rect x="29" y="26" width="10" height="8"/>
  </svg>
  <h3>IT Infrastructure<br>Design &amp; Installation</h3>
  <p>We can design and implement LANS/WANS and VPN's.&nbsp; Make your important data available to you wherever you are.</p>
</div>

<div class="office-photo" role="img" aria-label="Photo of a woman on the phone working at a wooden desk with a laptop in a sunny home office"></div>
<section class="flex-panel">
  <h2>Flexible solutions for<br>your business needs</h2>
  <div class="rule"></div>
  <p>Velmarketa is a technology solution provider based in Harbor City. Our goal is to make technology a non-issue for individuals and small to medium size businesses ranging from 5 to 150 Users. Velmarketa has the experience, the tools, high-level technology solutions and training to power your business and your work force. We understand that all business's have one goal in common!</p>
  <a class="btn" style="left:72px;top:292px;width:142px;height:44px">Learn More
    <svg viewBox="0 0 12 10" fill="none" stroke="#2b2f36" stroke-width="1.2"><path d="M0 5h11M7 1l4 4-4 4"/></svg>
  </a>
</section>

<section class="solutions">
  <h2 class="section-title" style="top:50px">IT Support Solutions</h2>
  <div class="title-rule" style="top:97px"></div>

  <div class="card" style="left:89px;top:128px">
    <svg viewBox="0 0 52 52" fill="none" stroke="#2b2f36" stroke-width="1.4"><rect x="6" y="2" width="40" height="11"/><rect x="6" y="17" width="40" height="11"/><rect x="6" y="32" width="40" height="8"/><path d="M26 40v6M4 48h44"/><circle cx="26" cy="48" r="2.5" fill="#fff"/><path d="M30 7h10M30 22h10"/></svg>
    <span>Network<br>Administration</span></div>
  <div class="card" style="left:294px;top:128px">
    <svg viewBox="0 0 52 52" fill="none" stroke="#2b2f36" stroke-width="1.4"><rect x="4" y="8" width="20" height="15"/><path d="M2 30h48M6 30v16M46 30v16"/><rect x="30" y="12" width="8" height="11"/><circle cx="44" cy="18" r="4"/><path d="M10 23v4h8v-4"/></svg>
    <span>Desktop<br>Support</span></div>
  <div class="card" style="left:498px;top:128px">
    <svg viewBox="0 0 52 52" fill="none" stroke="#2b2f36" stroke-width="1.4"><path d="M26 2v40M22 6l4-4 4 4M26 30l-10-7v-6M26 24l10-6v-5"/><circle cx="16" cy="15" r="2"/><rect x="34" y="9" width="4" height="4"/><circle cx="26" cy="45" r="4"/></svg>
    <span>Network<br>Cabling</span></div>
  <div class="card active" style="left:703px;top:128px">
    <svg viewBox="0 0 52 52" fill="none" stroke-width="1.4"><circle cx="26" cy="16" r="3" stroke="#2b2f36"/><path d="M26 19v31" stroke="#2b2f36"/><path d="M18 8a11 11 0 0 0 0 16M34 8a11 11 0 0 1 0 16M12 3a18 18 0 0 0 0 26M40 3a18 18 0 0 1 0 26" stroke="#f29b30"/></svg>
    <span>Wireles<br>Networks</span></div>
  <div class="card" style="left:908px;top:128px">
    <svg viewBox="0 0 52 52" fill="none" stroke="#2b2f36" stroke-width="1.4"><path d="M26 3l19 7v14c0 12-8 20-19 25C15 44 7 36 7 24V10z"/></svg>
    <span>Antivirus<br>Solutions</span></div>

  <div class="card" style="left:89px;top:316px">
    <svg viewBox="0 0 52 52" fill="none" stroke="#2b2f36" stroke-width="1.4"><path d="M10 12a22 22 0 0 1 32 0M15 17a15 15 0 0 1 22 0"/><rect x="16" y="30" width="20" height="18" rx="1"/><path d="M20 30v-5a6 6 0 0 1 12 0v5M26 37v5"/></svg>
    <span>Network<br>Security</span></div>
  <div class="card" style="left:294px;top:316px">
    <svg viewBox="0 0 52 52" fill="none" stroke="#2b2f36" stroke-width="1.4"><circle cx="26" cy="32" r="15"/><path d="M11 32h30M26 17v30M26 17c-7 5-7 25 0 30M26 17c7 5 7 25 0 30M26 17v-7"/><circle cx="26" cy="8" r="2"/><path d="M20 4a8 8 0 0 0 0 8M32 4a8 8 0 0 1 0 8"/></svg>
    <span>Telecommunication<br>Solutions</span></div>
  <div class="card" style="left:498px;top:316px">
    <svg viewBox="0 0 52 52" fill="none" stroke="#2b2f36" stroke-width="1.4"><path d="M42 20A17 17 0 0 0 11 16M10 32a17 17 0 0 0 31 4M11 8v8h8M41 44v-8h-8"/></svg>
    <span>Disaster<br>Recovery</span></div>
  <div class="card" style="left:703px;top:316px">
    <svg viewBox="0 0 52 52" fill="none" stroke="#2b2f36" stroke-width="1.4"><rect x="3" y="8" width="46" height="36"/><path d="M12 8v36M40 8v36M3 17h9M3 26h9M3 35h9M40 17h9M40 26h9M40 35h9M22 19v14l11-7z"/></svg>
    <span>Audio/Video<br>Multimedia</span></div>
  <div class="card" style="left:908px;top:316px">
    <svg viewBox="0 0 52 52" fill="none" stroke="#2b2f36" stroke-width="1.4"><rect x="4" y="4" width="44" height="44"/><path d="M4 12h44M9 20l2 7 2-5 2 5 2-7M19 20l2 7 2-5 2 5 2-7M29 20l2 7 2-5 2 5 2-7M10 34h32M10 40h24"/></svg>
    <span>Web<br>Design</span></div>
</section>

<footer class="site-footer">
  <h4 style="left:89px">Contact information</h4>
  <div class="info-item" style="top:98px"><svg viewBox="0 0 12 12"><path d="M6 0a4 4 0 0 1 4 4c0 3-4 8-4 8S2 7 2 4a4 4 0 0 1 4-4z" fill="#f29b30"/><circle cx="6" cy="4" r="1.5" fill="#2a303c"/></svg><span>Address:Some address line goes here. City name,<br>Country name here.</span></div>
  <div class="info-item" style="top:154px"><svg viewBox="0 0 12 12"><path d="M2 0l3 3-1.5 2c1 1.5 2 2.5 3.5 3.5L9 7l3 3-2 2C5 11 1 7 0 2z" fill="#f29b30"/></svg><span>Phone: 123 456 7890</span></div>
  <div class="info-item" style="top:190px"><svg viewBox="0 0 12 12"><rect x="0" y="2" width="12" height="8" fill="#f29b30"/><path d="M0 2l6 4 6-4" fill="none" stroke="#2a303c"/></svg><span>Email: info@velmarketa.com</span></div>
  <div class="info-item" style="top:225px"><svg viewBox="0 0 12 12"><rect x="3" y="0" width="6" height="3" fill="#f29b30"/><rect x="0" y="4" width="12" height="5" fill="#f29b30"/><rect x="3" y="8" width="6" height="4" fill="#f29b30"/></svg><span>Fax: 123 546 7890</span></div>

  <div class="divider"></div>

  <h4 style="left:622px">Contact now</h4>
  <div class="field-label" style="left:622px;top:101px">Name:</div>
  <div class="field-hint" style="left:622px;top:128px">Enter your name...</div>
  <div class="field-line" style="left:622px;top:149px;width:236px"></div>
  <div class="field-label" style="left:875px;top:101px">Email:</div>
  <div class="field-hint" style="left:875px;top:128px">Enter your email...</div>
  <div class="field-line" style="left:875px;top:149px;width:236px"></div>
  <div class="field-label" style="left:622px;top:168px">Message:</div>
  <div class="field-hint" style="left:622px;top:195px">Enter your message...</div>
  <div class="field-line" style="left:622px;top:243px;width:489px"></div>

  <div class="captcha"><span class="box"></span><span class="txt">I'm not a robot</span><span class="badge"></span></div>
  <div class="submit">Submit
    <svg width="12" height="10" viewBox="0 0 12 10" fill="none" stroke="#fff" stroke-width="1.2"><path d="M0 5h11M7 1l4 4-4 4"/></svg>
  </div>

  <div class="footer-rule"></div>
  <p class="copyright">© 2017, All Rights Reserved.</p>
</footer>

</body>
</html>
```